Website banner

Here is the link where the current banner is featured https://www.brimlark.com.au/collections/gel-blasters

I need the banner recreated into desktop and mobile format size.
Update the key points to:
- FREE SHIPPING AUSTRALIA WIDE
- SAME DAY DISPATCH
- BEST PRICE GUARANTEE
- 3000+ 5 STAR REVIEWS
- BEST SERVICE & WARRANTY
- 100% SECURE CHECKOUT

I want the banner to suit the style of the website and make it look better than the last graphic.

I also need the "save even more" picture to be recreated as it looks very plain at the moment,

```html
<!DOCTYPE html>
<html lang="en">
<head>
<meta charset="utf-8">
<title>Brimlark – Gel Blasters Banner</title>
<link href="https://fonts.googleapis.com/css2?family=Poppins:wght@400;500;600;700;800&display=swap" rel="stylesheet">
<style>
  :root {
    --page-bg: #f5f5f5;
    --brand-red: #ee2226;
    --brand-red-bright: #fb2326;
    --ribbon-red: #d63236;
    --ribbon-dark: #a8232a;
    --band-black: #0d0d0d;
    --camo-grey: #2a2a2a;
    --white: #ffffff;
    --row-light: #ececec;
    --row-mid: #d3d3d3;
    --ink: #111111;
    --gold: #f7b825;
  }
  * { margin: 0; padding: 0; box-sizing: border-box; }
  html, body {
    width: 762px; height: 1200px; overflow: hidden;
    background: var(--page-bg);
    font-family: "Poppins", sans-serif;
  }
  .canvas { position: relative; width: 762px; height: 1200px; }

  /* Key points banner */
  .usp-banner {
    position: absolute; left: 41px; top: 300px;
    width: 682px; height: 187px;
    background: radial-gradient(ellipse at 30% 80%, var(--camo-grey) 0%, var(--band-black) 55%), var(--band-black);
    box-shadow: 6px 8px 12px rgba(0,0,0,0.35);
    overflow: hidden;
  }
  .usp-banner__top {
    position: absolute; left: 0; top: 0; width: 100%; height: 74px;
    background: linear-gradient(90deg, var(--brand-red) 0%, var(--brand-red-bright) 50%, var(--brand-red) 100%);
  }
  .usp-banner__rule {
    position: absolute; left: 0; top: 74px; width: 100%; height: 4px;
    background: var(--white);
  }
  .usp {
    position: absolute; top: 48px; width: 120px; margin-left: -60px;
    text-align: center;
  }
  .usp__badge {
    width: 56px; height: 56px; margin: 0 auto;
    border-radius: 50%; background: var(--white);
    border: 3px solid var(--brand-red);
    box-shadow: 0 0 0 2px var(--white);
    display: flex; align-items: center; justify-content: center;
  }
  .usp__map {
    width: 40px; height: 34px; border-radius: 40% 50% 45% 40%;
    background: linear-gradient(160deg, #2538a8, #0d1f80);
  }
  .usp__label {
    margin-top: 12px; font-size: 9.6px; font-weight: 500;
    line-height: 12px; color: var(--white); letter-spacing: 0.1px;
  }
  .usp__label em { display: block; font-style: normal; color: var(--brand-red-bright); }

  /* Save even more ribbon */
  .savings {
    position: absolute; left: 174px; top: 640px; width: 416px; height: 196px;
  }
  .savings__ribbon { position: absolute; left: 0; top: 0; }
  .savings__title {
    position: absolute; left: 35px; top: 9px; width: 346px; height: 58px;
    display: flex; align-items: center; justify-content: center;
    color: var(--white); font-weight: 700; font-size: 31px; letter-spacing: 0.2px;
  }
  .savings__table {
    position: absolute; left: 38px; top: 67px; width: 340px;
    border-radius: 0 0 12px 12px; overflow: hidden;
    box-shadow: 0 6px 10px rgba(0,0,0,0.25);
  }
  .tier {
    height: 42px; display: flex; align-items: center; justify-content: center;
    font-size: 16.5px; font-weight: 500; color: var(--ink);
  }
  .tier strong { color: var(--brand-red); font-weight: 700; margin-left: 6px; }
  .tier--light { background: var(--row-light); }
  .tier--mid { background: var(--row-mid); }
  .tier--fade { background: linear-gradient(180deg, #f7f7f7, #e2e2e2); height: 43px; }
</style>
</head>
<body>
<main class="canvas">

  <section class="usp-banner" aria-label="Brimlark store key points">
    <div class="usp-banner__top"></div>
    <div class="usp-banner__rule"></div>

    <div class="usp" style="left:69px">
      <div class="usp__badge"><div class="usp__map" role="img" aria-label="Map of Australia with flag"></div></div>
      <p class="usp__label"><em>FREE SHIPPING</em>AUSTRALIA WIDE</p>
    </div>

    <div class="usp" style="left:178px">
      <div class="usp__badge">
        <svg width="36" height="30" viewBox="0 0 36 30" aria-hidden="true">
          <rect x="3" y="12" width="20" height="11" fill="#f7b825"/>
          <path d="M23 14h7l4 5v4H23z" fill="#e3242b"/>
          <rect x="25" y="15" width="5" height="3.5" fill="#fff"/>
          <circle cx="9" cy="24" r="3" fill="#333"/>
          <circle cx="29" cy="24" r="3" fill="#333"/>
          <circle cx="9" cy="8" r="6.5" fill="#e3242b"/>
          <path d="M9 4.5V8l2.5 1.5" stroke="#fff" stroke-width="1.4" fill="none"/>
        </svg>
      </div>
      <p class="usp__label"><em>SAME DAY</em>DISPATCH</p>
    </div>

    <div class="usp" style="left:286px">
      <div class="usp__badge">
        <svg width="42" height="42" viewBox="0 0 42 42" aria-hidden="true">
          <circle cx="21" cy="21" r="19" fill="#e3242b"/>
          <path d="M9 12l24-3-2 18-18 2-6 5 2-7z" fill="#f7b825"/>
          <text x="21" y="19" text-anchor="middle" font-family="Poppins, sans-serif" font-size="6.5" font-weight="800" fill="#fff">BEST</text>
          <text x="21" y="26" text-anchor="middle" font-family="Poppins, sans-serif" font-size="6.5" font-weight="800" fill="#fff">PRICE</text>
        </svg>
      </div>
      <p class="usp__label"><em>BEST PRICE</em>GUARANTEE</p>
    </div>

    <div class="usp" style="left:395px">
      <div class="usp__badge">
        <svg width="42" height="30" viewBox="0 0 42 30" aria-hidden="true">
          <defs><path id="star" d="M0-6l1.8 3.9 4.2.5-3.1 2.9.8 4.2L0 3.4l-3.7 2.1.8-4.2-3.1-2.9 4.2-.5z"/></defs>
          <g fill="#f7b825" stroke="#c98a00" stroke-width="0.6">
            <use href="#star" x="7" y="9"/><use href="#star" x="21" y="9"/><use href="#star" x="35" y="9"/>
            <use href="#star" x="14" y="21"/><use href="#star" x="28" y="21"/>
          </g>
        </svg>
      </div>
      <p class="usp__label"><em>3000+ 5</em>STAR REVIEWS</p>
    </div>

    <div class="usp" style="left:503px">
      <div class="usp__badge">
        <svg width="42" height="42" viewBox="0 0 42 42" aria-hidden="true">
          <path d="M21 2l4 4 5-1 2 5 5 2-1 5 4 4-4 4 1 5-5 2-2 5-5-1-4 4-4-4-5 1-2-5-5-2 1-5-4-4 4-4-1-5 5-2 2-5 5 1z" fill="#f7b825"/>
          <circle cx="21" cy="21" r="10" fill="#fff"/>
          <path d="M16 21l4 4 7-8" stroke="#e3242b" stroke-width="2.6" fill="none" stroke-linecap="round"/>
        </svg>
      </div>
      <p class="usp__label"><em>BEST SERVICE</em>&amp; WARRANTY</p>
    </div>

    <div class="usp" style="left:612px">
      <div class="usp__badge">
        <svg width="36" height="40" viewBox="0 0 36 40" aria-hidden="true">
          <path d="M18 2l15 5v11c0 10-7 17-15 20C10 35 3 28 3 18V7z" fill="#e3242b"/>
          <circle cx="18" cy="19" r="8" fill="#f7b825"/>
          <path d="M14 19l3 3 5-6" stroke="#fff" stroke-width="2.2" fill="none" stroke-linecap="round"/>
        </svg>
      </div>
      <p class="usp__label"><em>100% SECURE</em>CHECKOUT</p>
    </div>
  </section>

  <section class="savings" aria-label="Spend and save tiers">
    <svg class="savings__ribbon" width="416" height="70" viewBox="0 0 416 70" aria-hidden="true">
      <polygon points="0,0 58,2 58,58 0,58 22,29" fill="var(--ribbon-red)"/>
      <polygon points="416,0 358,2 358,58 416,58 394,29" fill="var(--ribbon-red)"/>
      <polygon points="35,0 58,6 58,10 35,9" fill="var(--ribbon-dark)"/>
      <polygon points="381,0 358,6 358,10 381,9" fill="var(--ribbon-dark)"/>
      <rect x="35" y="9" width="346" height="58" fill="var(--ribbon-red)"/>
      <rect x="35" y="9" width="14" height="58" fill="var(--ribbon-dark)" opacity="0.45"/>
      <rect x="367" y="9" width="14" height="58" fill="var(--ribbon-dark)" opacity="0.45"/>
    </svg>
    <h2 class="savings__title">SAVE EVEN MORE!</h2>
    <div class="savings__table">
      <p class="tier tier--light">ORDER $250+GET<strong>5% OFF</strong></p>
      <p class="tier tier--mid">ORDER $500+GET<strong>10% OFF</strong></p>
      <p class="tier tier--fade">ORDER $1000+GET<strong>15% OFF</strong></p>
    </div>
  </section>

</main>
</body>
</html>
```